Moder Business Card Design for Renewables Business

Need a business card design for my business. We collect & repurpose spent coffee ground from cafes. The cards will be made from recycled paper. Needs to fit our corporate colour scheme of white, green & brown (see logo for colour codes). Eco friendly, modern, intresting & eye catching.
This card needs to convey the message of the business and fit into its mantra of eco-friendly, sustainable etc.

Target Market(s)

Cafe Owners, Coffee Drinkers, Recycling Companies, Farmers

Industry/Entity Type

Recycling

Contact Information for Business Card

Name; Peter Dalton
Phone; 0438 216 570
e-mail; info@florivex.com.au
website; www.florivex.com.au

Font styles to use
Sans Serif
Script

Colors

Designer to choose colors to be used in the design.

Requirements
Must have
• FRONT;
• Logo, Name (Peter Dalton), phone number, e-mail address, website
• BACK;
• On the back in cursive text; 'GOOD GROUNDS FOR A GREENER DAY'
• Small facebook & Instagram logos with text 'Florivex'
Should not have
• messy design

```html
<!DOCTYPE html>
<html lang="en">
<head>
<meta charset="utf-8">
<title>Florivex Business Card</title>
<link rel="stylesheet" href="https://fonts.googleapis.com/css2?family=Didact+Gothic&family=Lobster&display=swap">
<style>
  :root {
    --bg: #d9d9d9;
    --paper: #fbfbfa;
    --leaf: #a3cd4b;
    --band-dark: #1f8c3d;
    --band-light: #3ea96d;
    --brown: #7b4a20;
    --brown-dark: #5b2d10;
    --ink: #1c1c1c;
    --rule: #777;
  }
  * { margin: 0; padding: 0; box-sizing: border-box; }
  html, body { width: 1200px; height: 864px; overflow: hidden; }
  body {
    background: var(--bg);
    font-family: "Didact Gothic", "Century Gothic", sans-serif;
    position: relative;
  }
  .card {
    position: absolute;
    left: 290px;
    width: 620px;
    height: 354px;
    background: var(--paper);
    box-shadow: 0 6px 18px rgba(0,0,0,.18);
    overflow: hidden;
  }
  .card--front { top: 44px; }
  .card--back { top: 466px; }

  /* Front */
  .brand-mark {
    position: absolute;
    left: 297px; top: 24px;
    width: 96px; height: 96px;
    border: 7px solid var(--brown);
    border-radius: 50%;
  }
  .brand-name {
    position: absolute;
    left: 220px; top: 128px;
    width: 250px;
    line-height: 36px;
    text-align: center;
    font-size: 30px;
    letter-spacing: 1px;
    color: var(--brown);
  }
  .person-name {
    position: absolute;
    left: 70px; top: 188px;
    font-size: 27px;
    line-height: 32px;
    color: var(--ink);
  }
  .divider {
    position: absolute;
    left: 274px; top: 180px;
    width: 1.5px; height: 78px;
    background: var(--rule);
  }
  .contact-list {
    position: absolute;
    left: 292px; top: 182px;
    list-style: none;
    font-size: 19px;
    color: var(--ink);
  }
  .contact-list li {
    display: flex; align-items: center;
    height: 25px;
  }
  .contact-list svg { width: 16px; height: 16px; margin-right: 10px; flex: none; }
  .band {
    position: absolute;
    left: 0; right: 0; top: 272px;
    height: 40px;
    background: linear-gradient(90deg, var(--band-dark), var(--band-light));
  }

  /* Back */
  .panel { position: absolute; }
  .panel--left { left: 0; top: 54px; }
  .panel--right { right: 0; top: 150px; }
  .back-mark {
    position: absolute;
    left: 240px; top: 64px;
    width: 120px; height: 120px;
    border: 7px solid var(--brown);
    border-radius: 50%;
    display: flex; align-items: center; justify-content: center;
    font-size: 22px;
    color: var(--brown);
  }
  .social-line {
    position: absolute;
    left: 100px; width: 400px; top: 204px;
    display: flex; justify-content: center; align-items: center;
    gap: 10px;
    font-size: 20px;
    line-height: 26px;
    color: var(--brown);
  }
  .social-dot {
    width: 16px; height: 16px;
    border-radius: 50%;
    background: var(--brown);
  }
  .tagline {
    position: absolute;
    left: 100px; width: 400px; top: 240px;
    text-align: center;
    font-family: "Lobster", cursive;
    font-size: 24px;
    line-height: 32px;
    color: var(--ink);
  }
</style>
</head>
<body>

<section class="card card--front" aria-label="Business card front">
  <div class="brand-mark"></div>
  <div class="brand-name">FLORIVEX</div>
  <div class="person-name">Peter Dalton</div>
  <div class="divider"></div>
  <ul class="contact-list">
    <li>
      <svg viewBox="0 0 16 16" aria-hidden="true"><path d="M4 1.5l2.2 3-1.3 1.5c.9 2 2.3 3.4 4.3 4.3l1.5-1.3 3 2.2-1.2 2.4C7 13.4 2.6 9 2.4 2.7z" fill="var(--band-dark)"/></svg>
      0438 216 570
    </li>
    <li>
      <svg viewBox="0 0 16 16" aria-hidden="true"><rect x="1" y="3.5" width="14" height="9" fill="var(--band-dark)"/><path d="M1 3.5l7 5 7-5" stroke="#fff" stroke-width="1.2" fill="none"/></svg>
      info@florivex.com.au
    </li>
    <li>
      <svg viewBox="0 0 16 16" aria-hidden="true"><circle cx="8" cy="8" r="6.5" fill="var(--band-dark)"/><path d="M1.5 8h13M8 1.5v13M3 4.5h10M3 11.5h10" stroke="#fff" stroke-width=".8"/><ellipse cx="8" cy="8" rx="3" ry="6.5" stroke="#fff" stroke-width=".8" fill="none"/></svg>
      www.florivex.com.au
    </li>
  </ul>
  <div class="band"></div>
</section>

<section class="card card--back" aria-label="Business card back">
  <svg class="panel panel--left" width="190" height="170" viewBox="0 0 190 170" aria-hidden="true">
    <rect x="0" y="0" width="188" height="3" fill="var(--brown-dark)"/>
    <path d="M0 12 H178 Q140 85 178 158 H0 Z" fill="var(--leaf)"/>
    <rect x="0" y="166" width="188" height="3" fill="var(--brown-dark)"/>
  </svg>
  <svg class="panel panel--right" width="170" height="170" viewBox="0 0 170 170" aria-hidden="true">
    <rect x="2" y="0" width="168" height="3" fill="var(--brown-dark)"/>
    <path d="M170 12 H12 Q48 85 12 158 H170 Z" fill="var(--leaf)"/>
    <rect x="2" y="166" width="168" height="3" fill="var(--brown-dark)"/>
  </svg>
  <div class="back-mark">Florivex</div>
  <div class="social-line"><span class="social-dot"></span>Florivex</div>
  <div class="tagline">Good grounds for a greener day</div>
</section>

</body>
</html>
```